Granite Ridge Response Business Card

Side 1: Granite Ridge Response Logo (logo without Maltese cross) with industrial rope rescue related theme. Our company services - TRAINING - Fire Training, Confined Space Rescue Training, Rope Rescue training, Hazmat Training, Incident Command, EMS, Pump Operations Training. Website - graniteridgeresponse.example.
Side 2: Granite Ridge Response Fire Department Logo (logo with Maltese cross) with Firefighter related theme. Company (division) services - FIELD SERVICES - Fire Department, Stand-by Rescue, Safety, EMS, Planning. "Supporting the Emergency Response Community Since 1967"

Add contact information wherever it makes since (Name, Email, Phone).
I would like it to represent the Granite Ridge Response Fire Department Logo as a division not as a separate entity without saying it, possibly by depicting it in the background of Side 2 instead of being a standalone picture like the logo on Side 1.

```html
<!DOCTYPE html>
<html lang="en">
<head>
<meta charset="utf-8">
<title>Granite Ridge Response Business Card</title>
<link href="https://fonts.googleapis.com/css2?family=Arimo:wght@400;700&family=Archivo:wght@700;800&display=swap" rel="stylesheet">
<style>
  :root {
    --bg: #e6e4e1;
    --red: #e30613;
    --white: #f4f4f4;
    --charcoal: #3b3b3e;
    --stroke: #3a3a3d;
    --ink-light: #ffffff;
    --ghost: rgba(255,255,255,0.06);
  }
  * { box-sizing: border-box; margin: 0; padding: 0; }
  html, body { width: 1200px; height: 960px; overflow: hidden; background: var(--bg); }
  body { position: relative; font-family: "Arimo", Arial, sans-serif; }

  .card {
    position: absolute; left: 220px; width: 760px; height: 434px;
    border-radius: 26px; overflow: hidden;
    box-shadow: 0 6px 18px rgba(0,0,0,0.18);
  }
  .card--front { top: 30px; background: var(--red); }
  .card--back { top: 496px; background: var(--charcoal); }

  .front-shape { position: absolute; inset: 0; }

  .contact { position: absolute; left: 46px; top: 40px; width: 290px; color: var(--ink-light); }
  .contact__name { font-family: "Archivo", Arial, sans-serif; font-weight: 800; font-size: 27px; text-transform: uppercase; letter-spacing: 0.2px; }
  .contact__title { font-size: 17px; margin-top: 2px; }
  .contact__address { font-size: 17px; line-height: 21px; margin-top: 10px; }
  .contact__list { list-style: none; margin-top: 8px; font-size: 17px; line-height: 21px; }
  .contact__list li { display: flex; align-items: center; gap: 8px; white-space: nowrap; }
  .contact__list svg { width: 13px; height: 13px; flex: none; }

  .training { position: absolute; left: 46px; top: 284px; width: 340px; color: var(--ink-light); font-size: 17px; line-height: 21px; }

  .brand { position: absolute; left: 470px; top: 178px; width: 260px; display: flex; align-items: center; gap: 12px; }
  .brand__mark { width: 22px; height: 22px; background: var(--red); flex: none; }
  .brand__name { font-family: "Archivo", Arial, sans-serif; font-weight: 800; font-size: 30px; line-height: 32px; color: var(--red); text-transform: uppercase; }

  .division-ghost {
    position: absolute; left: 40px; top: 110px; width: 340px;
    font-family: "Archivo", Arial, sans-serif; font-weight: 800; font-size: 52px; line-height: 56px;
    color: var(--ghost); text-transform: uppercase;
  }

  .services { position: absolute; left: 430px; top: 66px; color: var(--ink-light); }
  .services__heading { font-family: "Archivo", Arial, sans-serif; font-weight: 700; font-size: 24px; letter-spacing: 0.5px; }
  .services__list { margin: 16px 0 0 24px; font-size: 17px; line-height: 20px; }
  .services__tagline { margin: 16px 0 0 24px; font-size: 17px; line-height: 20px; width: 280px; }
</style>
</head>
<body>

<section class="card card--front" aria-label="Card front">
  <svg class="front-shape" viewBox="0 0 760 434" preserveAspectRatio="none" aria-hidden="true">
    <path d="M470 -4 L356 110 Q330 136 342 170 L452 440 L770 440 L770 -4 Z" fill="none" stroke="var(--stroke)" stroke-width="8" transform="translate(-14 0)"/>
    <path d="M470 -4 L356 110 Q330 136 342 170 L452 440 L770 440 L770 -4 Z" fill="var(--white)"/>
  </svg>

  <div class="contact">
    <div class="contact__name">Daniel Mercer</div>
    <div class="contact__title">President</div>
    <div class="contact__address">415 Quarry Ln., Fairhaven<br>TX, United States, 77000</div>
    <ul class="contact__list">
      <li><svg viewBox="0 0 16 16"><path fill="#fff" d="M3 1l3 3-1.5 2a9 9 0 0 0 5.5 5.5L12 10l3 3-2 2C7 15 1 9 1 3z"/></svg>+1 555-014-2237</li>
      <li><svg viewBox="0 0 16 16"><rect x="4" y="1" width="8" height="14" rx="1.5" fill="none" stroke="#fff" stroke-width="1.6"/></svg>+1 555-014-2237</li>
      <li><svg viewBox="0 0 16 16"><rect x="1" y="3" width="14" height="10" fill="#fff"/><path d="M1 3l7 6 7-6" fill="none" stroke="var(--red)" stroke-width="1.4"/></svg>dan@graniteridge.example</li>
      <li><svg viewBox="0 0 16 16"><circle cx="8" cy="8" r="7" fill="#fff"/><path d="M1 8h14M8 1c-3 3-3 11 0 14M8 1c3 3 3 11 0 14" fill="none" stroke="var(--red)" stroke-width="1"/></svg>www.graniteridgeresponse.example</li>
    </ul>
  </div>

  <p class="training">TRAINING - Fire Training<br>Confined Space Rescue Training<br>Rope Rescue training<br>Hazmat Training, Incident Command, EMS<br>Pump Operations Training.</p>

  <div class="brand">
    <span class="brand__mark"></span>
    <span class="brand__name">Granite Ridge Response</span>
  </div>
</section>

<section class="card card--back" aria-label="Card back">
  <div class="division-ghost" aria-hidden="true">Granite Ridge Response</div>
  <div class="services">
    <h2 class="services__heading">FIELD SERVICES</h2>
    <ul class="services__list">
      <li>Fire Department</li>
      <li>Stand-by Rescue</li>
      <li>Safety</li>
      <li>EMS</li>
      <li>Planning</li>
    </ul>
    <p class="services__tagline">Supporting the Emergency Response Community Since 1967</p>
  </div>
</section>

</body>
</html>
```